依頼詳細
海の家で開催するアコーステックライブのフライヤーです。

カフェやBarなど店舗に配布します。
開催まで日が少ないため早めに提案頂ける方、宜しくお願いします。

さわやか、ナチュラル、上品、20代~30代女性向け、オシャレな感じ

インスタグラム https://www.instagram.com/k72.note/
FB https://www.facebook.com/sunnyreefhut/

インスタやFBを見ていただき、雰囲気やテイストをイメージしていただければ幸いです。写真も必要であれば使ってください。

潮風の言葉に引っ張られず、自由にデザイン頂きたいです。
記載項目
開催概要
タイトル/潮風芸能祭Autumn Gala
日付/2016/09/11(SUN)
時間/OPEN/16:30 START/17:00 END/20:00
会場/海の家Sunny Reef Hut(佐賀県唐津市潮見町海水浴場)
LIVE/dawnrow/KORUE/MINT RIVER with WABELUK
TICKET/前売¥3,000- 当日¥4,000- 1Drink付
予約方法/①開催日 ②氏名 ③人数 ④連絡先電話番号をお伝えください。
連絡先/TEL080-7010-6213 MAIL info@sunnyreefhut.example

アーティスト情報は添付資料参照ください
サイズ
B6
ページ数
両面
希望イメージ
シンプル 複雑
単色 カラフル
暗い 明るい
日常 高級
遊び心 厳粛
未来的 伝統的
女性的 男性的
希望する色
納品ファイル
• 高解像度JPG (.jpg)
• イラストレーター形式 (.ai)
補足説明
■ 選んだ理由

スタッフの皆で協議の結果選定させていただきました。
ありがとうございました。

■ 提案者全員のお礼・コメント

今回ご提案いただきました皆様、どのデザインも良く、自分たちのイメージに沿った提案をいただき、選定に悩みました。
提案いただき本当にありがとうございました!
今後も機会があれば宜しくお願いします

```html
<!DOCTYPE html>
<html lang="ja">
<head>
<meta charset="utf-8">
<title>潮風芸能祭 Autumn Gala</title>
<link rel="stylesheet" href="https://fonts.googleapis.com/css2?family=Noto+Serif+JP:wght@500;700;900&family=Noto+Sans+JP:wght@400;700&family=Playfair+Display:wght@700&family=Oswald:wght@500&display=swap">
<style>
  :root {
    --sky-top: #2d3a4c;
    --sky-mid: #5a6677;
    --sunset: #e7b07a;
    --sea: #3a4a5e;
    --sand: #4a4038;
    --white: #ffffff;
    --logo-ink: #c9cdf5;
    --band-red: #b3263a;
    --band-blue: #263f8c;
    --live-red: #c4213a;
  }
  * { margin: 0; padding: 0; box-sizing: border-box; }
  html, body { width: 845px; height: 1200px; overflow: hidden; background: var(--sky-top); }
  .flyer {
    position: relative; width: 845px; height: 1200px; overflow: hidden;
    color: var(--white);
    font-family: "Noto Serif JP", serif;
  }
  .beach-photo {
    position: absolute; inset: 0 0 150px 0;
    background: linear-gradient(180deg, var(--sky-top) 0%, var(--sky-mid) 22%, var(--sunset) 31%, #8b8f98 34%, var(--sea) 45%, var(--sand) 72%, #231d1a 100%);
  }
  .logo {
    position: absolute; left: 0; right: 0; top: 70px; text-align: center;
  }
  .logo-name {
    font-family: "Playfair Display", serif; font-weight: 700;
    font-size: 64px; line-height: 1.1; color: var(--logo-ink);
  }
  .tagline {
    position: absolute; left: 28px; top: 420px;
    writing-mode: vertical-rl; font-size: 24px; letter-spacing: 5px;
    font-weight: 500; text-shadow: 0 0 6px rgba(0,0,0,.5);
  }
  .event-sub {
    position: absolute; top: 500px; width: 100%; text-align: center;
    font-family: "Playfair Display", serif; font-size: 34px; font-weight: 700; line-height: 1.2;
    text-shadow: 0 0 8px rgba(0,0,0,.5);
  }
  .event-title {
    position: absolute; top: 552px; width: 100%; text-align: center;
    font-size: 96px; font-weight: 900; letter-spacing: 6px; line-height: 1.1;
    text-shadow: 0 0 14px rgba(0,0,0,.55);
  }
  .event-date {
    position: absolute; top: 668px; left: 0; width: 100%; text-align: center;
    font-family: "Oswald", sans-serif; font-weight: 500; line-height: 1;
    text-shadow: 0 0 10px rgba(0,0,0,.5);
  }
  .event-date .year { font-size: 42px; margin-right: 10px; }
  .event-date .day { font-size: 92px; }
  .event-date .dow { font-size: 38px; margin-left: 6px; }
  .time-start {
    position: absolute; top: 768px; left: 420px; text-align: center;
    font-family: "Oswald", sans-serif; font-weight: 500; line-height: 1;
    text-shadow: 0 0 8px rgba(0,0,0,.5);
  }
  .time-start .label { font-size: 22px; display: block; margin-bottom: 2px; }
  .time-start .start { font-size: 50px; display: block; }
  .time-hours {
    position: absolute; top: 790px; left: 585px; text-align: right;
    font-family: "Oswald", sans-serif; font-weight: 500; font-size: 20px; line-height: 1.3;
    text-shadow: 0 0 8px rgba(0,0,0,.5);
  }
  .venue {
    position: absolute; top: 842px; left: 180px;
    font-weight: 700; text-shadow: 0 0 8px rgba(0,0,0,.6);
  }
  .venue .name { font-size: 38px; line-height: 1.2; white-space: nowrap; }
  .venue .name small { font-size: 24px; margin-right: 6px; }
  .venue .address { font-family: "Noto Sans JP", sans-serif; font-size: 21px; font-weight: 700; margin-left: 62px; line-height: 1.4; }
  .lineup {
    position: absolute; top: 942px; left: 24px; right: 20px;
    display: flex; align-items: center; gap: 14px; white-space: nowrap;
    font-family: "Noto Sans JP", sans-serif; font-weight: 700; font-size: 28px;
    text-shadow: 0 0 8px rgba(0,0,0,.6);
  }
  .live-badge {
    width: 58px; height: 58px; border-radius: 50%;
    background: var(--live-red); color: var(--white);
    display: flex; align-items: center; justify-content: center;
    font-size: 18px; text-shadow: none; flex: none;
  }
  .info-band {
    position: absolute; left: 0; right: 0; bottom: 0; height: 150px;
    background: linear-gradient(90deg, var(--band-red) 0%, #6a2f63 50%, var(--band-blue) 100%);
    padding: 14px 30px; font-family: "Noto Sans JP", sans-serif;
  }
  .ticket { text-align: right; font-size: 28px; font-weight: 700; line-height: 1.3; }
  .ticket small { font-size: 20px; }
  .booking { font-size: 20px; line-height: 1.6; margin-top: 6px; }
  .contact { display: flex; justify-content: space-between; font-size: 20px; line-height: 1.6; }
</style>
</head>
<body>
<div class="flyer">
  <div class="beach-photo" role="img" aria-label="夕暮れの海辺の海の家テラスと穏やかな海の写真"></div>

  <div class="logo"><span class="logo-name">Sunny Reef<br>Hut</span></div>

  <p class="tagline">ゆったりとした時間が流れる浜</p>

  <p class="event-sub">Autumn Gala</p>
  <h1 class="event-title">潮風芸能祭</h1>

  <p class="event-date"><span class="year">2016</span><span class="day">9/11</span><span class="dow">(SUN)</span></p>

  <div class="time-start"><span class="label">START</span><span class="start">17:00</span></div>
  <div class="time-hours">OPEN/16:30<br>END/20:00</div>

  <div class="venue">
    <div class="name"><small>会場</small>海の家Sunny Reef Hut</div>
    <div class="address">(佐賀県唐津市潮見町海水浴場)</div>
  </div>

  <div class="lineup">
    <span class="live-badge">LIVE</span>
    <span>dawnrow／KORUE／MINT RIVER with WABELUK</span>
  </div>

  <div class="info-band">
    <p class="ticket">TICKET／前売¥3,000､当日¥4,000､<small>1 Drink付</small></p>
    <p class="booking">予約方法／①開催日 ②氏名 ③人数 ④連絡先電話番号をお伝えください。</p>
    <p class="contact"><span>連絡先／TEL:090-4825-3917</span><span>MAIL: info@sunnyreefhut.example</span></p>
  </div>
</div>
</body>
</html>
```